Marlowe Hairdressing Business Card Design

The design has to be based upon a colour scheme of a black gloss background and silver type face letters and has to portray an exclusive and expensive outlet.

The business card has a dual use with the rear of the card being used for future appointments therefore this area has to be lined out to accept written text.

We also need to incorporate a Chatterbook log somewhere on the card.

Target Market(s)

High Earning individuals with high disposable incomes possible link too young professionals.

Contact Information for Business Card

Marlowe Hairdressing & The Willowmere Beauty
Tel 01632 418550
www.marlowehairdressing.example.co.uk

Requirements
Must have
• Company Name including beauty element, telephone number, website and chatterbook please.
Nice to have
• High Gloss finish with silver raised letters or similar
Should not have
• Hairdressing Images like, scissors, haircuts, beauty treatments etc

```html
<!DOCTYPE html>
<html lang="en">
<head>
<meta charset="utf-8">
<title>Marlowe Hairdressing – Business Card</title>
<link href="https://fonts.googleapis.com/css2?family=Jost:wght@300;400&display=swap" rel="stylesheet">
<style>
  :root {
    --page: #ffffff;
    --card-black: #050505;
    --gloss-light: #5a5a5a;
    --gloss-dark: #1a1a1a;
    --silver: #c9c9c9;
    --silver-dim: #8c8c8c;
    --silver-faint: #3b3b3b;
    --panel-grey: #bdbdbd;
    --rule: #7a7a7a;
  }
  html, body {
    margin: 0;
    width: 1200px;
    height: 1200px;
    overflow: hidden;
    background: var(--page);
  }
  .canvas {
    position: relative;
    width: 1200px;
    height: 1200px;
    font-family: "Jost", "Helvetica Neue", Arial, sans-serif;
  }
  .card {
    position: absolute;
    left: 210px;
    width: 780px;
    height: 516px;
    background: var(--card-black);
    overflow: hidden;
  }
  .card--front { top: 54px; }
  .card--back { top: 630px; }

  .gloss-arc {
    position: absolute;
    left: 0; top: 0;
    width: 780px; height: 516px;
  }
  .front-text {
    position: absolute;
    left: 0;
    width: 100%;
    text-align: center;
    color: var(--silver);
    font-weight: 300;
    margin: 0;
  }
  .front-text--mark {
    top: 72px;
    font-size: 26px;
    letter-spacing: 8px;
    color: var(--silver);
  }
  .front-text--name {
    top: 196px;
    font-size: 30px;
    letter-spacing: 3px;
    text-transform: uppercase;
  }
  .front-text--amp {
    top: 262px;
    font-size: 26px;
    color: var(--silver-dim);
  }
  .front-text--beauty {
    top: 306px;
    font-size: 24px;
    letter-spacing: 3px;
    color: var(--silver-dim);
  }
  .front-text--tel {
    top: 434px;
    font-size: 24px;
    letter-spacing: 2px;
    color: var(--silver-dim);
  }

  .back-watermark {
    position: absolute;
    left: 60px;
    top: 40px;
    font-size: 150px;
    font-weight: 300;
    color: var(--silver-faint);
    letter-spacing: 4px;
    margin: 0;
    line-height: 1;
  }
  .appointment-panel {
    position: absolute;
    left: 70px;
    top: 86px;
    width: 650px;
    height: 232px;
    background: var(--panel-grey);
    opacity: 0.95;
  }
  .appointment-line {
    position: absolute;
    left: 38px;
    right: 38px;
    height: 1px;
    background: var(--rule);
  }
  .social {
    position: absolute;
    left: 352px;
    top: 352px;
    display: flex;
    align-items: center;
    gap: 10px;
    color: var(--silver);
    font-size: 20px;
    font-weight: 400;
  }
  .social__square {
    width: 34px;
    height: 34px;
    background: var(--silver);
  }
  .web {
    position: absolute;
    left: 0;
    width: 100%;
    top: 432px;
    text-align: center;
    color: var(--silver-dim);
    font-size: 22px;
    font-weight: 300;
    letter-spacing: 2.5px;
    margin: 0;
  }
</style>
</head>
<body>
<main class="canvas">

  <section class="card card--front" aria-label="Business card front">
    <svg class="gloss-arc" viewBox="0 0 780 516" aria-hidden="true">
      <defs>
        <linearGradient id="arcGloss" x1="0" y1="0" x2="1" y2="0">
          <stop offset="0" stop-color="#2a2a2a"/>
          <stop offset="0.45" stop-color="#585858"/>
          <stop offset="0.6" stop-color="#4a4a4a"/>
          <stop offset="1" stop-color="#1c1c1c"/>
        </linearGradient>
        <linearGradient id="arcFade" x1="0" y1="0" x2="0" y2="1">
          <stop offset="0" stop-color="#000" stop-opacity="0"/>
          <stop offset="1" stop-color="#000" stop-opacity="0.85"/>
        </linearGradient>
      </defs>
      <path d="M0 400 Q 390 200 780 400 L780 516 L0 516 Z" fill="url(#arcGloss)"/>
      <path d="M0 400 Q 390 200 780 400 L780 516 L0 516 Z" fill="url(#arcFade)"/>
    </svg>
    <p class="front-text front-text--mark">MARLOWE</p>
    <p class="front-text front-text--name">Marlowe Hairdressing</p>
    <p class="front-text front-text--amp">&amp;</p>
    <p class="front-text front-text--beauty">The Willowmere Beauty</p>
    <p class="front-text front-text--tel">Tel 01632 418550</p>
  </section>

  <section class="card card--back" aria-label="Business card back, appointment card">
    <p class="back-watermark" aria-hidden="true">Marlowe</p>
    <div class="appointment-panel" aria-label="Appointment lines">
      <span class="appointment-line" style="top:58px"></span>
      <span class="appointment-line" style="top:101px"></span>
      <span class="appointment-line" style="top:144px"></span>
      <span class="appointment-line" style="top:188px"></span>
    </div>
    <div class="social">
      <span class="social__square" aria-hidden="true"></span>
      <span class="social__name">the marlowe hairdressing</span>
    </div>
    <p class="web">www.marlowehairdressing.example.co.uk</p>
  </section>

</main>
</body>
</html>
```